CONTACT US Page and design for website

We need a contact us page for our website. We would like it to have a message area, a map, our information, etc.

Please see the text attachment for what we are looking for. We need to have something that is creative and interesting, modern and professional.

We believe that a contact US page should be very creative because everyone clicks that to contact us. We want it to be super professional, attention grabbing, pleasing to the eye.

PLEASE KEEP THE HEADER AND FOOTER THE SAME, ONLY THE ACTUAL CONTACT US PAGE NEEDS TO BE WORKED ON. THANKS!
We are excited to work with designers for this project.

Target Market(s)

Clients in technology business

Industry/Entity Type

Information Technology

Number of Pages Required

1 page

Font styles to use
Serif

Requirements
Must have
• CHECK THE TEXT ATTACHMENT PLEASE
• Must stay within our design colors and theme.
Nice to have
• see attachment
Should not have
• it should be special

```html
<!DOCTYPE html>
<html lang="en">
<head>
<meta charset="utf-8">
<title>Contact Us – Novaline Tech</title>
<link rel="stylesheet" href="https://fonts.googleapis.com/css2?family=Roboto:wght@300;400;500;700&display=swap">
<style>
:root{
  --teal:#35c2b1;
  --teal-dark:#25a797;
  --ink:#333;
  --muted:#777;
  --line:#dcdcdc;
  --foot:#8a8b8e;
  --foot-dark:#6c6d70;
  --white:#fff;
}
*{box-sizing:border-box;margin:0;padding:0}
html,body{width:764px;height:1200px;overflow:hidden;background:var(--white)}
body{font-family:"Roboto",sans-serif;color:var(--ink);position:relative}
.page{position:relative;width:764px;height:1200px}
/* header */
.header{position:absolute;top:0;left:0;width:764px;height:84px;background:var(--white);border-bottom:1px solid #eee}
.brand-name{position:absolute;left:26px;top:16px;font-size:20px;font-weight:500;color:var(--teal)}
.top-tools{position:absolute;right:26px;top:18px;display:flex;gap:16px;align-items:center;font-size:9px;color:var(--muted)}
.top-tools .phone{color:var(--teal);font-weight:700;font-size:11px}
.nav{position:absolute;left:26px;right:26px;top:58px;display:flex;align-items:center;gap:13px;font-size:7.5px;color:#555;font-weight:500;letter-spacing:.3px;white-space:nowrap}
.search{margin-left:auto;width:84px;height:16px;border:1px solid var(--line);border-radius:2px;font-size:7px;color:#aaa;padding:3px 6px}
/* breadcrumb */
.crumb{position:absolute;top:84px;left:0;width:764px;height:30px;background:var(--teal);color:var(--white);font-size:9px;font-weight:500;padding:10px 38px;letter-spacing:.5px}
/* map */
.map{position:absolute;top:114px;left:0;width:764px;height:334px;background:linear-gradient(160deg,#ecebe6,#dedbd3)}
.map-card{position:absolute;left:438px;top:142px;width:176px;height:98px;background:var(--white);box-shadow:0 2px 6px rgba(0,0,0,.25);padding:9px 10px;font-size:7px;line-height:1.5;color:#555}
.map-card h4{font-size:8px;font-weight:700;color:#333}
.map-card .link{color:#3a7bd5;margin-top:6px}
.map-card:after{content:"";position:absolute;left:80px;bottom:-8px;border:8px solid transparent;border-bottom:0;border-top-color:var(--white)}
.pin{position:absolute;left:510px;top:262px}
.pin-label{position:absolute;left:528px;top:268px;font-size:7px;color:#555}
/* contact section */
.contact{position:absolute;top:448px;left:0;width:764px;height:260px}
.col-title{font-size:12px;font-weight:500;color:#333;letter-spacing:.4px;padding-bottom:9px;border-bottom:1px solid var(--line);margin-bottom:14px;white-space:nowrap}
.form{position:absolute;left:38px;top:28px;width:346px}
.field{height:18px;border:1px solid var(--line);font-size:7px;color:#999;padding:5px 8px;margin-bottom:8px}
.field.msg{height:64px}
.submit{width:54px;height:18px;background:var(--teal);color:var(--white);font-size:7px;font-weight:700;text-align:center;line-height:18px;border-radius:2px}
.hours{position:absolute;left:412px;top:28px;width:188px}
.hours li{list-style:none;font-size:8.5px;color:#444;margin-bottom:10px;display:flex;align-items:center;gap:8px}
.hours li:before{content:"";width:6px;height:6px;border-radius:50%;background:var(--teal)}
.note{margin-top:10px;display:flex;gap:8px;align-items:center;font-size:8px;color:var(--teal-dark);line-height:1.4}
.note-icon{flex:none;width:22px;height:22px;border-radius:50%;background:var(--teal)}
.social{position:absolute;left:626px;top:28px;width:112px}
.social .dots{display:flex;gap:5px}
.social .dots span{width:20px;height:20px;border-radius:50%;background:var(--teal)}
.social .dots span:nth-child(even){background:var(--foot-dark)}
/* contact info band */
.info{position:absolute;top:738px;left:0;width:764px;height:160px;background:var(--teal);color:var(--white)}
.info h2{text-align:center;font-size:22px;font-weight:400;letter-spacing:1px;margin-top:16px}
.info-cols{position:absolute;top:64px;left:38px;right:38px;display:flex;justify-content:space-between}
.info-col{width:210px;display:flex;gap:10px}
.info-col svg{flex:none}
.info-col h3{font-size:13px;font-weight:400;margin-bottom:6px}
.info-col p{font-size:7.5px;line-height:2}
/* footer */
.footer{position:absolute;top:898px;left:0;width:764px;height:184px;background:var(--foot);color:var(--white);text-align:center}
.footer .blurb{width:520px;margin:18px auto 0;font-size:7.5px;line-height:1.6}
.footer .contacts{display:flex;justify-content:center;gap:60px;margin-top:16px;font-size:7.5px;line-height:1.5}
.footer .links{display:flex;justify-content:center;gap:38px;margin-top:20px;font-size:10px;font-weight:500}
.footer .links small{display:block;font-size:6.5px;font-weight:400;line-height:1.5;margin-top:2px}
.bottom{position:absolute;top:1082px;left:0;width:764px;height:118px;background:var(--foot-dark);color:var(--white);text-align:center}
.bottom .dots{display:flex;justify-content:center;gap:14px;margin-top:14px}
.bottom .dots span{width:20px;height:20px;border-radius:50%;border:1px solid rgba(255,255,255,.7)}
.bottom .mark{margin-top:20px;font-size:10px;font-weight:500}
.bottom .copy{font-size:6.5px;margin-top:5px;opacity:.85}
.chat-tab{position:absolute;right:8px;bottom:0;width:82px;height:18px;background:var(--teal);color:var(--white);font-size:7px;font-weight:500;text-align:center;line-height:18px;border-radius:3px 3px 0 0}
</style>
</head>
<body>
<div class="page">
  <header class="header">
    <div class="brand-name">Novaline Tech</div>
    <div class="top-tools"><span>LIVE CHAT</span><span class="phone">555-010-0142</span></div>
    <nav class="nav">
      <span>NETWORK</span><span>WORKSTATIONS</span><span>COMPONENTS</span><span>VIRTUAL REALITY</span><span>DRONES</span><span>ABOUT US</span><span>BLOG</span><span>RESOURCES</span><span>CONTACT US</span>
      <span class="search">Search</span>
    </nav>
  </header>

  <div class="crumb">HOME / CONTACT US</div>

  <div class="map" role="img" aria-label="Street map showing the office location"></div>
  <div class="map-card">
    <h4>OFFICE HEADQUARTERS</h4>
    NOVALINE TECH LLC<br>1200 Cedar Ave<br>Fairview, CA 90100
    <div class="link">View larger map</div>
  </div>
  <svg class="pin" width="14" height="20" viewBox="0 0 14 20"><path d="M7 0C3 0 0 3 0 7c0 5 7 13 7 13s7-8 7-13c0-4-3-7-7-7z" fill="#e4453a"/><circle cx="7" cy="7" r="2.5" fill="#fff"/></svg>
  <span class="pin-label">1200 Cedar Avenue</span>

  <section class="contact">
    <div class="form">
      <h2 class="col-title">CONTACT US</h2>
      <div class="field">Name</div>
      <div class="field">Phone No.</div>
      <div class="field">E-mail</div>
      <div class="field msg">Message</div>
      <div class="submit">SUBMIT</div>
    </div>
    <div class="hours">
      <h2 class="col-title">HOURS OF OPERATION</h2>
      <ul>
        <li>Monday: 8:00am - 5:00pm</li>
        <li>Tuesday: 8:00am - 5:00pm</li>
        <li>Wednesday: 8:00am - 5:00pm</li>
        <li>Thursday: 8:00am - 5:00pm</li>
        <li>Friday: 8:00am - 5:00pm</li>
      </ul>
      <div class="note"><span class="note-icon"></span>Our dedicated customer service representatives are available 24/7 by phone.</div>
    </div>
    <div class="social">
      <h2 class="col-title">STAY CONNECTED</h2>
      <div class="dots"><span></span><span></span><span></span><span></span></div>
    </div>
  </section>

  <section class="info">
    <h2>CONTACT INFO</h2>
    <div class="info-cols">
      <div class="info-col">
        <svg width="40" height="34" viewBox="0 0 40 34"><path d="M0 0h40L20 34z" fill="#fff"/></svg>
        <div><h3>General Inquiries</h3><p>&#9742; (555)010-0142</p><p>&#9993; info@novaline.example</p></div>
      </div>
      <div class="info-col">
        <svg width="40" height="34" viewBox="0 0 40 34"><path d="M0 0h40L20 34z" fill="#fff"/></svg>
        <div><h3>Sales Inquiries</h3><p>&#9742; (555)010-0142</p><p>&#9993; sales@novaline.example</p></div>
      </div>
      <div class="info-col">
        <svg width="40" height="34" viewBox="0 0 40 34"><path d="M0 0h40L20 34z" fill="#fff"/></svg>
        <div><h3>Purchasing Inquiries</h3><p>&#9742; (555)010-0177</p><p>&#9993; buying@novaline.example</p></div>
      </div>
    </div>
  </section>

  <footer class="footer">
    <p class="blurb">Based in Fairview, California, Novaline Tech offers custom servers, storage, and workstations for local businesses in nearby cities and counties. Novaline Tech also offers tech products to clients throughout the United States and worldwide.</p>
    <div class="contacts">
      <span>1200 Cedar Ave<br>Fairview, CA 90100</span>
      <span>(555)010-0142</span>
      <span>sales@novaline.example</span>
    </div>
    <div class="links">
      <span>Computer Hardware</span><span>Drones</span><span>Virtual Reality</span><span>About Us</span>
      <span>Customer Support<small>Terms and Conditions<br>Return Policy<br>Privacy Policy</small></span>
    </div>
  </footer>
  <div class="bottom">
    <div class="dots"><span></span><span></span><span></span><span></span></div>
    <div class="mark">Novaline Tech</div>
    <div class="copy">Novaline Tech LLC<br>Copyright © 2017</div>
  </div>
  <div class="chat-tab">Leave a message</div>
</div>
</body>
</html>
```